Business card design for holistic health care clinic

We need a double-sided business card design for our holistic health care clinic that integrates our logo design and also its color scheme. My business is called Veralune. It is an integrative medicine clinic. You have already done the logo for me. Please ensure an elegant and upscale design that is not cluttered, but still has all the necessary information (please see below for details).

Target Market(s)

Wellness, fitness, rehabilitation for educated, well-traveled open-minded clients who are focused on natural, organic, balanced and preventive healthcare and lifestyle.

Industry/Entity Type

Medical

Contact Information for Business Card

Modern, clean.

Number of Pages Required

1 page

Font styles to use
Serif
Sans Serif

Colors

Designer to choose colors to be used in the design.

Requirements
Must have
• Logo on one side, all other information on the other side.
• Other information should include:
• Tobias Wendmere - DOE, CPT, LMT
• 1450 North Calloway Street
• Austin, TX 78744
• 512 555 0184
• 818 555 0127
• info@VeraluneHealth.com
• t.wendmere@VeraluneHealth.com
Nice to have
• Darker background on front - but not totally black - shaded/dark gray.

```html
<!DOCTYPE html>
<html lang="en">
<head>
<meta charset="utf-8">
<title>Veralune Business Card</title>
<link rel="stylesheet" href="https://fonts.googleapis.com/css2?family=PT+Sans:ital,wght@0,400;0,700;1,400;1,700&display=swap">
<style>
  :root {
    --backdrop: #3b3430;
    --card: #1c1d1f;
    --card-edge: #26282b;
    --brand-blue: #1f8fd0;
    --text-light: #e6e6e6;
    --text-muted: #b9bcc0;
    --rule: #9a9da1;
  }
  * { margin: 0; padding: 0; box-sizing: border-box; }
  html, body {
    width: 1200px; height: 864px; overflow: hidden;
    background: var(--backdrop);
    font-family: "PT Sans", Arial, sans-serif;
  }
  .sheet {
    width: 1200px; height: 864px;
    display: flex; flex-direction: column; align-items: center; justify-content: center;
    gap: 32px;
  }
  .card {
    position: relative;
    width: 680px; height: 388px;
    background: linear-gradient(160deg, var(--card-edge), var(--card));
    box-shadow: 0 10px 28px rgba(0,0,0,.45);
  }
  /* Front side */
  .front .brand {
    position: absolute; left: 0; right: 0; top: 88px;
    text-align: center; color: var(--brand-blue);
  }
  .brand-name {
    font-weight: 700; font-size: 78px; letter-spacing: 2px;
    line-height: 1; text-transform: uppercase;
  }
  .brand-descriptor {
    font-weight: 700; font-size: 25px; margin-top: 6px; letter-spacing: .3px;
  }
  .front .tagline-row {
    position: absolute; left: 70px; right: 70px; top: 270px;
    display: flex; align-items: center; gap: 14px;
  }
  .tagline-row .rule { flex: 1; height: 1px; background: var(--rule); }
  .tagline {
    font-style: italic; font-size: 19px; color: var(--text-muted);
  }
  /* Back side */
  .back .holder {
    position: absolute; left: 40px; top: 42px;
    color: var(--brand-blue); font-weight: 700; font-style: italic;
    font-size: 20px; text-transform: uppercase;
  }
  .holder .credentials { font-size: 13px; font-weight: 400; font-style: italic; }
  .contact-list {
    position: absolute; left: 40px; top: 82px; list-style: none;
  }
  .contact-list li {
    display: flex; align-items: center; gap: 10px;
    color: var(--text-light); font-size: 18px; line-height: 27px;
  }
  .contact-list svg { width: 14px; height: 14px; fill: var(--brand-blue); flex: none; }
  .back .brand {
    position: absolute; right: 40px; top: 44px; text-align: right; color: var(--brand-blue);
  }
  .back .brand-name { font-size: 54px; letter-spacing: 1.5px; }
  .back .brand-descriptor { font-size: 17px; margin-top: 4px; }
  .back .divider {
    position: absolute; left: 40px; right: 40px; top: 220px;
    height: 1px; background: var(--rule);
  }
  .address {
    position: absolute; right: 40px; bottom: 46px; text-align: right;
    font-style: normal; color: var(--text-light); font-size: 20px; line-height: 28px;
  }
</style>
</head>
<body>
<main class="sheet">
  <section class="card front" aria-label="Card front">
    <div class="brand">
      <div class="brand-name">Veralune</div>
      <div class="brand-descriptor">Integrative Holistic Medicine</div>
    </div>
    <div class="tagline-row">
      <span class="rule"></span>
      <span class="tagline">helping the body help itself</span>
      <span class="rule"></span>
    </div>
  </section>

  <section class="card back" aria-label="Card back">
    <div class="holder">Tobias Wendmere <span class="credentials">- DOE, CPT, LMT</span></div>
    <ul class="contact-list">
      <li>
        <svg viewBox="0 0 16 16" aria-hidden="true"><path d="M3.6 1.2l2.3 2.6-1.3 1.9c.9 2 2.5 3.6 4.5 4.6l1.9-1.3 2.6 2.3-1.4 2.5C7 13.6 2.4 9 1.2 3z"/></svg>
        512 555 0184
      </li>
      <li>
        <svg viewBox="0 0 16 16" aria-hidden="true"><path d="M4 1h8v14H4zM5.5 2.5v9h5v-9zM7 12.5h2v1H7z" fill-rule="evenodd"/></svg>
        818 555 0127
      </li>
      <li>
        <svg viewBox="0 0 16 16" aria-hidden="true"><path d="M1 3h14v10H1zm1.5 1.4v.4L8 8.6l5.5-3.8v-.4z"/></svg>
        t.wendmere@VeraluneHealth.com
      </li>
      <li>
        <svg viewBox="0 0 16 16" aria-hidden="true"><circle cx="8" cy="8" r="7"/></svg>
        www.VeraluneHealth.com
      </li>
    </ul>
    <div class="brand">
      <div class="brand-name">Veralune</div>
      <div class="brand-descriptor">Integrative Holistic Medicine</div>
    </div>
    <div class="divider"></div>
    <address class="address">
      1450 North Calloway Street<br>
      Austin, TX 78744
    </address>
  </section>
</main>
</body>
</html>
```